Copper Wren (short term rental)

This website will be for a short term rental (lodge h&h) located in a small quant town called Medicine Park and at the entrance of the Tallow Creek Reserve. I am currently in a logo contest and will have the logo soon to use on the website My goal for the website is to highlight the home and area with photographs, text, and possibly a rotating video/slide show of the local area. I will soon have a professional photographer at the home and will upload my own photos to the site with your instructions. I want a booking option for customers to use vs hosting sites like KELZ and lodge h&H. . I would like copperwren.org ( or .com—-appreciate your guidance here) for the web address. And I want it to appear on search engines with words like, medicine park, medicine park rental, rental near Wichita mountains, etc. I hope you can help me. Thanks!

Target Market(s)

Outdoor enthusiasts (bikers, hikers, lakers, etc) festival attendees, hippies.

Industry/Entity Type

Short term rental

Coding

Coded - Design and coding required

Number of Pages Required

1 page

Font styles to use
Serif

Colors
00AB8E
00BBA5
67D7C9
C6EFE9
E9F9F6

Requirements
Must have
• Booking calendar, reviews section, contact us section, brief over view of the area, place to upload my photos

```html
<!DOCTYPE html>
<html lang="en">
<head>
<meta charset="utf-8">
<title>Copper Wren – Short-term Rental in Medicine Park</title>
<link href="https://fonts.googleapis.com/css2?family=Playfair+Display:wght@400;700;800&family=Montserrat:wght@600;700;800&family=Lato:wght@400;700&display=swap" rel="stylesheet">
<style>
:root{
  --green:#1aa783;
  --green-dark:#12906f;
  --teal:#00bba5;
  --mint:#67d7c9;
  --mint-pale:#e9f9f6;
  --grey-bg:#f2f2f3;
  --ink:#2b2b2b;
  --muted:#555;
  --footer:#1e1f22;
  --white:#fff;
}
*{box-sizing:border-box;margin:0;padding:0}
html,body{width:1200px;height:5245px;overflow:hidden}
body{font-family:"Lato",Arial,sans-serif;color:var(--ink);background:var(--white);position:relative}
.abs{position:absolute}
.section{position:absolute;left:0;width:1200px}
.serif{font-family:"Playfair Display",Georgia,serif}
.heading{font-family:"Montserrat",Arial,sans-serif;font-weight:800;color:var(--green);text-transform:uppercase;text-align:center;font-size:22px;letter-spacing:.5px;width:1200px;left:0}
.rule{width:40px;height:2px;background:#555;left:580px}
.photo{position:absolute}

/* header */
.site-header{top:0;height:78px;background:var(--white)}
.logo{left:134px;top:22px;font-family:"Playfair Display",Georgia,serif;font-size:25px;color:#222}
.nav{left:403px;top:30px;display:flex;gap:0;font-size:13px}
.nav a{color:#333;text-decoration:none;margin-right:26px;position:relative}
.nav a.active{color:var(--green)}
.nav a.active::after{content:"";position:absolute;left:-4px;right:-4px;bottom:-8px;height:2px;background:var(--green)}
.call{left:890px;top:0;width:310px;height:78px;background:var(--green);clip-path:polygon(0 0,100% 0,100% 100%,0 100%)}
.call-icon{left:872px;top:22px;width:48px;height:34px;background:var(--mint);display:flex;align-items:center;justify-content:center}
.call-text{left:940px;top:22px;color:#fff;font-size:15px;line-height:18px}
.call-text b{font-family:"Montserrat",sans-serif;font-size:11px;display:block}

/* hero */
.hero{top:78px;height:570px;background:linear-gradient(180deg,#7d8a8f 0%,#5b6a5f 25%,#6a3a2c 55%,#4a2e22 80%,#3b3a2a 100%)}
.hero h1{left:0;width:1200px;top:48px;text-align:center;color:#fff;font-family:"Playfair Display",Georgia,serif;font-weight:800;font-size:42px;line-height:52px}
.booking{left:167px;top:458px;width:820px;height:58px;display:flex;gap:3px}
.booking .field{background:rgba(255,255,255,.85);display:flex;align-items:center;gap:8px;padding:0 16px;font-size:13px;color:#333;height:58px}
.booking .btn{background:var(--green);color:#fff;font-family:"Montserrat",sans-serif;font-weight:700;font-size:12px;display:flex;align-items:center;justify-content:center;width:100px;height:42px;margin:8px 0 0 8px}

/* rental */
.rental{top:648px;height:639px}
.rental-box{left:546px;top:38px;width:521px;height:550px;background:var(--green)}
.rental-img{left:130px;top:102px;width:503px;height:383px;background:linear-gradient(160deg,#2d3a52 0%,#3c4150 40%,#4a5a3a 75%,#2f4a25 100%)}
.rental h2{left:674px;top:76px;width:360px;color:#fff;font-family:"Montserrat",sans-serif;font-weight:800;font-size:24px;line-height:30px}
.rental .bar{left:676px;top:152px;width:60px;height:2px;background:#fff}
.rental p{left:676px;top:183px;width:335px;color:#fff;font-size:15px;line-height:20px}
.read-more{left:678px;top:495px;width:100px;height:39px;background:#fff;color:var(--green);font-family:"Montserrat",sans-serif;font-weight:700;font-size:11px;display:flex;align-items:center;justify-content:center}
.carousel{left:258px;top:538px;display:flex;align-items:center;gap:14px}
.dot{width:5px;height:5px;border-radius:50%;background:#444}

/* facilities */
.facilities{top:1287px;height:640px;background:var(--grey-bg)}
.tabs{left:132px;top:136px;display:flex;gap:38px;font-family:"Montserrat",sans-serif;font-weight:700;font-size:13px}
.tabs .on{color:var(--green);border-bottom:2px solid var(--green);padding-bottom:6px}
.amenities{left:132px;top:178px;width:316px;list-style:none}
.amenities li{height:34.4px;border-bottom:1px solid #d6d6d6;display:flex;align-items:center;gap:12px;font-size:13.5px;padding-left:8px}
.fac-img{left:546px;top:114px;width:521px;height:471px;background:linear-gradient(135deg,#f4f3ef 0%,#e6e4dd 50%,#cfd3cf 100%)}

/* neighborhood */
.neighborhood{top:1927px;height:479px;background:linear-gradient(180deg,#6f8aa0 0%,#9bb0b8 22%,#56683f 50%,#3d4b2c 100%)}
.neighborhood h2{left:0;width:1200px;top:168px;text-align:center;color:#fff;font-family:"Montserrat",sans-serif;font-weight:800;font-size:38px;letter-spacing:1px}
.neigh-box{left:218px;top:289px;width:762px;height:190px;background:#fff;padding:38px 60px 0;text-align:center;font-size:15.5px;line-height:22.5px;color:#444}

/* gallery */
.gallery{top:2406px;height:876px}
.g{background:#999}
.view-all{left:526px;top:794px;width:146px;height:39px;background:var(--green);color:#fff;font-family:"Montserrat",sans-serif;font-weight:700;font-size:11px;display:flex;align-items:center;justify-content:center}

/* reviews */
.reviews{top:3282px;height:513px;background:var(--mint-pale)}
.card{top:128px;width:224px;height:338px;background:#fff;padding:24px 26px;font-size:12.2px;line-height:17px;color:#555;box-shadow:0 1px 4px rgba(0,0,0,.06)}
.card .q{color:var(--green);font-family:"Playfair Display",serif;font-size:40px;font-weight:700;text-align:center;line-height:28px;margin-bottom:10px}
.card .stars{color:var(--green);font-size:12px;letter-spacing:1px;margin-top:12px}
.card .name{font-size:12px;color:#555}

/* overview */
.overview{top:3795px;height:629px}
.circle{left:138px;width:145px;height:145px;border-radius:50%}
.ov-block{left:324px;width:744px}
.ov-block h3{font-family:"Montserrat",sans-serif;font-weight:700;font-size:13px;color:#222;margin-bottom:14px}
.ov-block p{font-size:11px;line-height:12.2px;color:#333;text-align:justify}
.ov-block ol{list-style:none;font-size:11px;line-height:24px;color:#333}

/* contact */
.contact{top:4424px;height:471px;background:linear-gradient(180deg,#1fa67f 0%,#1e9b73 60%,#238a62 100%)}
.contact h2{color:#fff}
.input{background:#fff;font-size:11.5px;color:#333;padding:12px 14px}
.submit{left:538px;top:379px;width:124px;height:43px;background:var(--mint);color:#fff;font-family:"Montserrat",sans-serif;font-weight:800;font-size:16px;display:flex;align-items:center;justify-content:center}

/* footer */
.footer{top:4895px;height:350px;background:var(--footer);color:#fff}
.footer .brand{left:134px;top:110px;font-family:"Playfair Display",Georgia,serif;font-size:30px}
.footer h4{font-family:"Montserrat",sans-serif;font-weight:700;font-size:13px}
.f-item{display:flex;gap:14px;font-size:11.5px;line-height:14px;margin-bottom:18px}
.f-menu{list-style:none;font-size:11px;line-height:24px}
.social{display:flex;gap:12px;align-items:center;font-size:11px;line-height:13px;margin-bottom:22px}
.social .c{width:22px;height:22px;border-radius:50%;background:#1d6fd6;flex:none}
.copy{left:0;width:1200px;top:304px;text-align:center;font-size:11.5px}
</style>
</head>
<body>

<header class="section site-header">
  <div class="abs logo">Copper Wren</div>
  <nav class="abs nav">
    <a class="active" href="#">Home</a><a href="#">About us</a><a href="#">Rooms</a><a href="#">Blog</a><a href="#">Reviews</a><a href="#">Contact us</a>
  </nav>
  <div class="abs call"></div>
  <div class="abs call-icon">
    <svg width="22" height="22" viewBox="0 0 24 24" fill="none" stroke="#fff" stroke-width="1.6"><path d="M5 3h4l2 5-2.5 1.5a11 11 0 0 0 6 6L16 13l5 2v4a2 2 0 0 1-2 2A17 17 0 0 1 3 5a2 2 0 0 1 2-2z"/></svg>
  </div>
  <div class="abs call-text"><b>GIVE US A CALL</b>+1 580 555 0142</div>
</header>

<section class="section hero">
  <div class="photo" role="img" aria-label="Photo of large timber mountain lodge beneath rocky peaks" style="inset:0"></div>
  <h1 class="abs">Short-term rental Home<br>in Wichita Mountains</h1>
  <div class="abs booking">
    <div class="field" style="width:200px"><svg width="16" height="16" viewBox="0 0 24 24" fill="none" stroke="#333" stroke-width="1.8"><path d="M12 22s7-7 7-12a7 7 0 0 0-14 0c0 5 7 12 7 12z"/><circle cx="12" cy="10" r="2.5"/></svg>Destination</div>
    <div class="field" style="width:124px"><svg width="16" height="16" viewBox="0 0 24 24" fill="none" stroke="#333" stroke-width="1.8"><rect x="3" y="5" width="18" height="16"/><path d="M3 10h18M8 3v4M16 3v4"/></svg>Check In</div>
    <div class="field" style="width:128px"><svg width="16" height="16" viewBox="0 0 24 24" fill="none" stroke="#333" stroke-width="1.8"><rect x="3" y="5" width="18" height="16"/><path d="M3 10h18M8 3v4M16 3v4"/></svg>Check Out</div>
    <div class="field" style="width:128px"><svg width="18" height="16" viewBox="0 0 24 20" fill="none" stroke="#333" stroke-width="1.8"><path d="M2 18V3M2 12h20v6M22 12V9a3 3 0 0 0-3-3h-9v6"/></svg>Rooms<span style="margin-left:auto">▾</span></div>
    <div class="field" style="width:124px"><svg width="16" height="16" viewBox="0 0 24 24" fill="none" stroke="#333" stroke-width="1.8"><circle cx="12" cy="8" r="4"/><path d="M4 21c0-4 4-6 8-6s8 2 8 6"/></svg>Guests<span style="margin-left:auto">▾</span></div>
    <div class="btn">BOOK NOW</div>
  </div>
</section>

<section class="section rental">
  <div class="abs rental-box"></div>
  <div class="abs rental-img" role="img" aria-label="Photo of stone rental home at dusk with lit windows and garden"></div>
  <h2 class="abs">RENTAL HOME IN MEDICINE PARK</h2>
  <div class="abs bar"></div>
  <p class="abs">Sed ut perspiciatis unde omnis iste natus error sit voluptatem accusantium doloremque laudantium, totam rem aperiam, eaque ipsa quae ab illo inve ntore veritatis et quasi architecto beatae vitae dicta sunt explicabo. Nemo enim ipsam volup tatem quia voluptas sit aspernatur aut odit aut fugit, sed quia consequuntur magni dolores eos qui ratione voluptatem sequi nesciunt. Neque porro quisquam est, qui dolorem ipsum quia dolor sit amet, consectetur, adipisci velit, sed quia non numquam eius modi tempora incidunt ut labore et dolore magnam aliquam quaerat voluptatem</p>
  <div class="abs read-more">READ MORE</div>
  <div class="abs carousel">
    <svg width="14" height="30" viewBox="0 0 14 30" fill="none" stroke="#777" stroke-width="1.5"><path d="M13 1L1 15l12 14"/></svg>
    <span class="dot"></span><span class="dot"></span><span class="dot"></span><span class="dot"></span><span class="dot"></span>
    <svg width="14" height="30" viewBox="0 0 14 30" fill="none" stroke="#777" stroke-width="1.5"><path d="M1 1l12 14L1 29"/></svg>
  </div>
</section>

<section class="section facilities">
  <h2 class="abs heading" style="top:38px">Facilities</h2>
  <div class="abs rule" style="top:78px"></div>
  <div class="abs tabs"><span class="on">COMMUNITY AMENITIES</span><span>HOME AMENITIES</span></div>
  <ul class="abs amenities">
    <li><svg width="12" height="10" viewBox="0 0 12 10"><path d="M1 5l3.5 3.5L11 1" fill="none" stroke="#1aa783" stroke-width="2.4"/></svg>Fitness Center</li>
    <li><svg width="12" height="10" viewBox="0 0 12 10"><path d="M1 5l3.5 3.5L11 1" fill="none" stroke="#1aa783" stroke-width="2.4"/></svg>Basketball Court</li>
    <li><svg width="12" height="10" viewBox="0 0 12 10"><path d="M1 5l3.5 3.5L11 1" fill="none" stroke="#1aa783" stroke-width="2.4"/></svg>Hammock Garden</li>
    <li><svg width="12" height="10" viewBox="0 0 12 10"><path d="M1 5l3.5 3.5L11 1" fill="none" stroke="#1aa783" stroke-width="2.4"/></svg>Bark Park w/ Agility Course</li>
    <li><svg width="12" height="10" viewBox="0 0 12 10"><path d="M1 5l3.5 3.5L11 1" fill="none" stroke="#1aa783" stroke-width="2.4"/></svg>On-site maintenance</li>
    <li><svg width="12" height="10" viewBox="0 0 12 10"><path d="M1 5l3.5 3.5L11 1" fill="none" stroke="#1aa783" stroke-width="2.4"/></svg>Sunning Deck</li>
    <li><svg width="12" height="10" viewBox="0 0 12 10"><path d="M1 5l3.5 3.5L11 1" fill="none" stroke="#1aa783" stroke-width="2.4"/></svg>Poolside Pergola Lounge</li>
    <li><svg width="12" height="10" viewBox="0 0 12 10"><path d="M1 5l3.5 3.5L11 1" fill="none" stroke="#1aa783" stroke-width="2.4"/></svg>Fire Pit</li>
    <li><svg width="12" height="10" viewBox="0 0 12 10"><path d="M1 5l3.5 3.5L11 1" fill="none" stroke="#1aa783" stroke-width="2.4"/></svg>Coffee Bar</li>
    <li><svg width="12" height="10" viewBox="0 0 12 10"><path d="M1 5l3.5 3.5L11 1" fill="none" stroke="#1aa783" stroke-width="2.4"/></svg>Free Wi-Fi in Clubhouse and Fitness Center</li>
    <li><svg width="12" height="10" viewBox="0 0 12 10"><path d="M1 5l3.5 3.5L11 1" fill="none" stroke="#1aa783" stroke-width="2.4"/></svg>BBQ/Picnic Area</li>
    <li><svg width="12" height="10" viewBox="0 0 12 10"><path d="M1 5l3.5 3.5L11 1" fill="none" stroke="#1aa783" stroke-width="2.4"/></svg>Resort-Style Swimming Pool</li>
  </ul>
  <div class="abs fac-img" role="img" aria-label="Photo of bright white modern kitchen"></div>
</section>

<section class="section neighborhood">
  <div class="photo" role="img" aria-label="Photo of forested rocky canyon under a cloudy sky" style="inset:0"></div>
  <h2 class="abs">NEIGHBORHOOD</h2>
  <div class="abs neigh-box">Sed ut perspiciatis unde omnis iste natus error sit voluptatem accusantium doloremque laudantium, totam rem aperiam, eaque ipsa quae ab illo inve ntore veritatis et quasi architecto beatae vitae dicta sunt explicabo. Nemo enim ipsam volup tatem quia voluptas sit aspernatur aut odit aut fugit, sed quia consequuntur magni dolores eos qui ratione voluptatem sequi nesciunt. Neque porro quisquam est, qui dolorem ipsum quia dolor sit amet, consectetur, adipisci velit, sed quia non numquam eius modi tempora incidunt ut labore et dolore magnam aliquam quaerat voluptatem</div>
</section>

<section class="section gallery">
  <h2 class="abs heading" style="top:80px">Photo Gallery</h2>
  <div class="abs rule" style="top:124px"></div>
  <div class="photo g" role="img" aria-label="Photo of dim living room with tall windows" style="left:130px;top:167px;width:560px;height:393px;background:linear-gradient(160deg,#4a4238,#7a6650 45%,#2e2a26)"></div>
  <div class="photo g" role="img" aria-label="Photo of grey living room with fireplace" style="left:703px;top:167px;width:364px;height:193px;background:linear-gradient(135deg,#dcdcdc,#9a9a9a 60%,#6b4a34)"></div>
  <div class="photo g" role="img" aria-label="Photo of lounge with glass wall and garden view" style="left:703px;top:368px;width:364px;height:192px;background:linear-gradient(135deg,#e2ddd3,#b6a58b 50%,#6f7d4f)"></div>
  <div class="photo g" role="img" aria-label="Photo of light kitchen with wooden stools" style="left:130px;top:574px;width:306px;height:190px;background:linear-gradient(135deg,#f3ede4,#d8c3a5 60%,#a98660)"></div>
  <div class="photo g" role="img" aria-label="Photo of bathroom with glass shower" style="left:446px;top:574px;width:306px;height:190px;background:linear-gradient(135deg,#f1f1ef,#c9cac7 55%,#6f6d68)"></div>
  <div class="photo g" role="img" aria-label="Photo of infinity pool overlooking a city" style="left:762px;top:574px;width:305px;height:190px;background:linear-gradient(180deg,#9fc4e6 0%,#c9dcea 40%,#3aa6cf 70%,#3f6f3a 100%)"></div>
  <div class="abs view-all">VIEW ALL IMAGES</div>
</section>

<section class="section reviews">
  <h2 class="abs heading" style="top:38px">Reviews</h2>
  <div class="abs rule" style="top:83px"></div>
  <svg class="abs" style="left:64px;top:272px" width="14" height="30" viewBox="0 0 14 30" fill="none" stroke="#888" stroke-width="1.5"><path d="M13 1L1 15l12 14"/></svg>
  <svg class="abs" style="left:1114px;top:272px" width="14" height="30" viewBox="0 0 14 30" fill="none" stroke="#888" stroke-width="1.5"><path d="M1 1l12 14L1 29"/></svg>
  <div class="abs card" style="left:132px"><div class="q">&ldquo;</div>Nemo enim ipsam volup tatem quia voluptas sit aspernatur aut odit aut fugit, sed quia conseq uuntur magni dolores eos qui ratione voluptatem sequi nesc iunt. Neque porro quisquam est, qui dolorem ipsum quia dolor sit amet, consectetur, adipisci velit, sed quia non numquam eius modi tempora incidunt ut labore et dolore magnam aliquam.<div class="stars">★★★★★</div><div class="name">Dana Hollis</div></div>
  <div class="abs card" style="left:369px"><div class="q">&ldquo;</div>Nemo enim ipsam volup tatem quia voluptas sit aspernatur aut odit aut fugit, sed quia conseq uuntur magni dolores eos qui ratione voluptatem sequi nesc iunt. Neque porro quisquam est, qui dolorem ipsum quia dolor sit amet, consectetur, adipisci velit, sed quia non numquam eius modi tempora incidunt ut labore et dolore magnam aliquam.<div class="stars">★★★★★</div><div class="name">Dana Hollis</div></div>
  <div class="abs card" style="left:607px"><div class="q">&ldquo;</div>Nemo enim ipsam volup tatem quia voluptas sit aspernatur aut odit aut fugit, sed quia conseq uuntur magni dolores eos qui ratione voluptatem sequi nesc iunt. Neque porro quisquam est, qui dolorem ipsum quia dolor sit amet, consectetur, adipisci velit, sed quia non numquam eius modi tempora incidunt ut labore et dolore magnam aliquam.<div class="stars">★★★★★</div><div class="name">Dana Hollis</div></div>
  <div class="abs card" style="left:845px"><div class="q">&ldquo;</div>Nemo enim ipsam volup tatem quia voluptas sit aspernatur aut odit aut fugit, sed quia conseq uuntur magni dolores eos qui ratione voluptatem sequi nesc iunt. Neque porro quisquam est, qui dolorem ipsum quia dolor sit amet, consectetur, adipisci velit, sed quia non numquam eius modi tempora incidunt ut labore et dolore magnam aliquam.<div class="stars">★★★★★</div><div class="name">Dana Hollis</div></div>
</section>

<section class="section overview">
  <div class="abs circle" role="img" aria-label="Photo of a monument against blue sky" style="top:55px;background:radial-gradient(circle at 50% 40%,#8fb6d9,#4f7fae 60%,#5b4a3a)"></div>
  <div class="abs ov-block" style="top:55px">
    <h3>OVERVIEW MEDICINE PARK</h3>
    <p>At vero eos et accusamus et iusto odio dignissimos ducimus qui blanditiis praesentium voluptatum deleniti atque corrupti quos dolores et quas molestias excepturi sint occaecati cupiditate non provident, similique sunt in culpa qui officia deserunt mollitia animi, id est laborum et dolorum fuga. Et harum quidem rerum facilis est et expedita distinctio. Nam libero tempore, cum soluta nobis est eligendi optio cumque nihil impedit quo minus id quod maxime placeat facere possimus, omnis voluptas assumenda est, omnis dolor repellendus. Temporibus autem quibusdam et aut officiis debitis aut rerum necessitatibus saepe eveniet ut et voluptates repudiandae sint et molestiae non recusandae. Itaque earum rerum hic tenetur a sapiente On the other hand, we denounce with righteous indignation and dislike men who are so beguiled and demoralized by the charms of pleasure of the moment, so blinded by desire, that they cannot foresee the pain and trouble that are bound to ensue; and equal blame belongs to those who fail in their duty through weakness of will, which is the same as saying through shrinking from toil and pain. These cases are perfectly simple</p>
  </div>
  <div class="abs circle" role="img" aria-label="Photo of green hills at sunset" style="top:248px;background:radial-gradient(circle at 50% 30%,#e9b6a4,#7a8f5a 55%,#3f5a2e)"></div>
  <div class="abs ov-block" style="top:252px">
    <h3>RENTAL NEAR WICHITA MOUNTAINS</h3>
    <p>At vero eos et accusamus et iusto odio dignissimos ducimus qui blanditiis praesentium voluptatum deleniti atque corrupti quos dolores et quas molestias excepturi sint occaecati cupiditate non provident, similique sunt in culpa qui officia deserunt mollitia animi, id est laborum et dolorum fuga. Et harum quidem rerum facilis est et expedita distinctio. Nam libero tempore, cum soluta nobis est eligendi optio cumque nihil impedit quo minus id quod maxime placeat facere possimus, omnis voluptas assumenda est, omnis dolor repellendus. Temporibus autem quibusdam et aut officiis debitis aut rerum necessitatibus saepe eveniet ut et voluptates repudiandae sint et molestiae non recusandae. Itaque earum rerum hic tenetur a sapiente On the other hand, we denounce with righteous indignation and dislike men who are so beguiled and demoralized by the charms of pleasure of the moment, so blinded by desire, that they cannot foresee the pain and trouble that are bound to ensue; and equal blame belongs to those who fail in their duty through weakness of will, which is the same as saying through shrinking from toil and pain. These cases are perfectly simple</p>
  </div>
  <div class="abs circle" role="img" aria-label="Photo of lake at sunset" style="top:444px;background:radial-gradient(circle at 50% 45%,#f2b877,#c4685a 50%,#3d3a4a)"></div>
  <div class="abs ov-block" style="top:458px">
    <h3>LOCAL ATTRACTIONS</h3>
    <ol>
      <li>1. Tallow Creek Reserve</li>
      <li>2. Medicine Park, OK, Riverstone Aquarium and Science Center</li>
      <li>3. Fort Harlow, OK, National Landmark and Museum</li>
      <li>4. Redbank National Museum and Cultural Center</li>
    </ol>
  </div>
</section>

<section class="section contact">
  <div class="photo" role="img" aria-label="Green-tinted photo of open prairie with bison" style="inset:0;background:linear-gradient(180deg,rgba(255,255,255,0) 50%,rgba(0,60,30,.18))"></div>
  <h2 class="abs heading" style="top:40px;color:#fff">Contact Us</h2>
  <div class="abs input" style="left:267px;top:123px;width:324px;height:38px">First Name</div>
  <div class="abs input" style="left:603px;top:123px;width:326px;height:38px">Last Name</div>
  <div class="abs input" style="left:267px;top:173px;width:324px;height:41px">Email id</div>
  <div class="abs input" style="left:603px;top:173px;width:326px;height:41px">Phone</div>
  <div class="abs input" style="left:267px;top:228px;width:662px;height:125px">Message</div>
  <div class="abs submit">SUBMIT</div>
</section>

<footer class="section footer">
  <div class="abs brand">Copper Wren</div>
  <div class="abs" style="left:458px;top:40px;width:230px">
    <h4 style="margin-bottom:22px">CONTACT US</h4>
    <div class="f-item"><svg width="16" height="16" viewBox="0 0 24 24"><circle cx="12" cy="12" r="12" fill="#1aa783"/><path d="M12 18s4-4 4-7a4 4 0 0 0-8 0c0 3 4 7 4 7z" fill="#fff"/></svg><span>418 Granite Ridge Road,<br>Suite #12, Alder Falls, OK 73999</span></div>
    <div class="f-item"><svg width="16" height="16" viewBox="0 0 24 24"><circle cx="12" cy="12" r="12" fill="#1aa783"/><path d="M8 6h2.5l1 3-1.5 1a6 6 0 0 0 3 3l1-1.5 3 1V15a1.5 1.5 0 0 1-1.5 1.5A8.5 8.5 0 0 1 6.5 7.5 1.5 1.5 0 0 1 8 6z" fill="#fff"/></svg><span>Call Us<br>+1 580 555 0142</span></div>
    <div class="f-item"><svg width="16" height="16" viewBox="0 0 24 24"><circle cx="12" cy="12" r="12" fill="#1aa783"/><rect x="6" y="8" width="12" height="8" fill="#fff"/><path d="M6 8l6 5 6-5" fill="none" stroke="#1aa783" stroke-width="1.3"/></svg><span>E mail Us<br>info@copperwren.org</span></div>
  </div>
  <div class="abs" style="left:758px;top:40px">
    <h4 style="margin-bottom:12px">MENU</h4>
    <ul class="f-menu"><li>HOME</li><li>ABOUT US</li><li>ROOMS</li><li>BLOG</li><li>REVIEWS</li><li>CONTACT US</li></ul>
  </div>
  <div class="abs" style="left:966px;top:40px">
    <h4 style="margin-bottom:22px">FOLLOW US</h4>
    <div class="social"><span class="c"></span><span>Like us on<br>FRIENDBOOK</span></div>
    <div class="social"><span class="c"></span><span>Follow us on<br>CHIRPER</span></div>
    <div class="social"><span class="c"></span><span>Follow us on<br>WORKLINK</span></div>
  </div>
  <div class="abs copy">Copyright © 2022 All Rights Reserved</div>
</footer>

</body>
</html>
```